Business Card Design Project

Hi Designers, this project is currently on hold until the Logo is completed:
Please submit to the Logo project here:
http://work.pitchvault.example/brief.aspx?id=413907

Once logo is completed, it will be attached to this project for you to create business cards with show logo, company name and address

Maren T R Quillby

Osric's Tiny Grey Heron Co.
Fernbrook
Nether Coombsby
North Devon EX91 4TZ

Tel: 01809 417356
Mobile: 07900 263818
email: maren@tiny-grey-heron.example.co.uk

Project Deadline Extended
Reason: Sorry everyone, we have had a sick ewe and I am now behind with this one and need to extend the deadline. Best wishes Maren

The designer who wins the logo brief will be asked to design the business card. Many thanks Maren

Project Deadline Extended
Reason: Sorry everyone, just a chaotic time of year with animals. Need to extend the deadline again..... as I just haven't had enough time to take a good look.... Thank you for your understanding. Maren

Project Deadline Extended
Reason: Sorry everyone It is our busiest time of year with animals and just no time to spend going through such great designs. I will have to extend the deadline again and hopefully have some news very soon. Wishing you all a very happy Christmas and a happy and healthy new year. Maren & Osric

High end market
Boutique restaurants for meat (it's not commercial lamb it's a slow matured quality meat more like venison/beef) expensive - specialized market

High End shoot clothing / wool / sheepskin rugs
Quality products

Business

• based on the logo - (which Pitch Vault has just been asked to do)
possibly based on a simplified picture of a Hebridean Ram (shows it's a Hebridean by it's horns as opposed to other black sheep!!)

```html
<!DOCTYPE html>
<html lang="en">
<head>
<meta charset="utf-8">
<title>Osric's Tiny Grey Heron Co. — Business Card</title>
<link href="https://fonts.googleapis.com/css2?family=Arimo:wght@400;700&display=swap" rel="stylesheet">
<style>
  :root {
    --page: #e9e7e3;
    --card-white: #ffffff;
    --card-dark: #262a2b;
    --band: #46494c;
    --ink: #3a3d40;
    --ink-soft: #55585b;
    --rule: #5a5d60;
    --light-text: #f4f4f4;
  }
  * { box-sizing: border-box; margin: 0; padding: 0; }
  html, body { width: 1200px; height: 1037px; overflow: hidden; }
  body {
    background: var(--page);
    font-family: "Arimo", Arial, sans-serif;
    position: relative;
  }
  .card {
    position: absolute;
    left: 210px;
    width: 780px;
    height: 446px;
    box-shadow: 0 6px 18px rgba(0,0,0,0.18);
    overflow: hidden;
  }
  .card--front { top: 50px; background: var(--card-white); }
  .card--back { top: 541px; background: var(--card-dark); }

  /* front */
  .brand {
    position: absolute;
    left: 48px;
    top: 112px;
    display: flex;
    align-items: center;
    gap: 16px;
    color: var(--ink);
  }
  .brand__circle {
    width: 62px; height: 62px;
    border: 5px solid var(--ink);
    border-radius: 50%;
    flex: none;
  }
  .brand__name {
    font-weight: 400;
    color: var(--ink);
    line-height: 1.15;
  }
  .brand__name .line-main { display: block; font-size: 30px; letter-spacing: 1px; }
  .brand__name .line-sub { display: block; font-size: 11.5px; letter-spacing: 1.6px; }

  .divider {
    position: absolute;
    left: 340px;
    top: 38px;
    width: 2px;
    height: 282px;
    background: var(--rule);
  }
  .person {
    position: absolute;
    left: 390px;
    top: 64px;
    color: var(--ink);
  }
  .person__name { font-size: 29px; font-weight: 400; }
  .person__role { font-size: 15px; margin-top: 4px; color: var(--ink-soft); }

  .contacts {
    position: absolute;
    left: 380px;
    top: 198px;
    list-style: none;
    font-size: 18px;
    color: var(--ink);
  }
  .contacts li {
    display: flex;
    align-items: center;
    gap: 12px;
    height: 28px;
  }
  .contacts svg { width: 16px; height: 16px; flex: none; fill: var(--ink); }

  .address-band {
    position: absolute;
    left: 0; right: 0; bottom: 0;
    height: 96px;
    background: var(--band);
    border-top: 10px solid var(--card-white);
    box-shadow: inset 0 3px 0 var(--band);
    display: flex;
    align-items: center;
    justify-content: center;
    color: var(--light-text);
    font-size: 19px;
    letter-spacing: 0.3px;
  }

  /* back */
  .back-mark {
    position: absolute;
    left: 50%;
    top: 54px;
    transform: translateX(-50%);
    display: flex;
    flex-direction: column;
    align-items: center;
    color: var(--light-text);
  }
  .back-mark__circle {
    width: 200px; height: 200px;
    border: 14px solid var(--light-text);
    border-radius: 50%;
  }
  .back-mark__name {
    margin-top: 22px;
    text-align: center;
    font-weight: 400;
    color: var(--light-text);
    line-height: 1.15;
  }
  .back-mark__name .line-main { display: block; font-size: 46px; letter-spacing: 2px; }
  .back-mark__name .line-sub { display: block; font-size: 17px; letter-spacing: 3px; }
</style>
</head>
<body>

<section class="card card--front" aria-label="Business card front">
  <div class="brand">
    <span class="brand__circle"></span>
    <p class="brand__name">
      <span class="line-main">OSRIC'S</span>
      <span class="line-sub">TINY GREY HERON CO.</span>
    </p>
  </div>

  <div class="divider"></div>

  <div class="person">
    <h1 class="person__name">Maren T R Quillby</h1>
    <p class="person__role">CEO</p>
  </div>

  <ul class="contacts">
    <li>
      <svg viewBox="0 0 16 16" aria-hidden="true"><path d="M3.2 1.5l2.4 2.6-1.2 1.8c.9 2 2.6 3.7 4.6 4.6l1.8-1.2 2.6 2.4-1.4 2.3C7 13.5 2.5 9 1 3z"/></svg>
      <span>01809 417356</span>
    </li>
    <li>
      <svg viewBox="0 0 16 16" aria-hidden="true"><path d="M4 1h8v14H4zM5.6 2.8v9.2h4.8V2.8z"/></svg>
      <span>07900 263818</span>
    </li>
    <li>
      <svg viewBox="0 0 16 16" aria-hidden="true"><path d="M1 3h14v10H1zM2.5 4.4v.4L8 9l5.5-4.2v-.4z"/></svg>
      <span>maren@tiny-grey-heron.example.co.uk</span>
    </li>
    <li>
      <svg viewBox="0 0 16 16" aria-hidden="true"><circle cx="8" cy="8" r="7"/></svg>
      <span>www.osrictinygreyheron.example.com</span>
    </li>
  </ul>

  <div class="address-band">
    <p>Fernbrook, Nether Coombsby, North Devon EX91 4TZ</p>
  </div>
</section>

<section class="card card--back" aria-label="Business card back">
  <div class="back-mark">
    <span class="back-mark__circle"></span>
    <p class="back-mark__name">
      <span class="line-main">OSRIC'S</span>
      <span class="line-sub">TINY GREY HERON CO.</span>
    </p>
  </div>
</section>

</body>
</html>
```